Webdesign für psychotherapeutische Praxis
Zielgruppe
Psychotherapeutische Praxis für erwachsene Patienten mit psychischen Erkrankungen.
Die Website soll eine solide, vertrauensvolle Information über das therapeutische Angebot bieten sowie alle Informationen zur Erstkontaktaufnahme erhalten.
Aufgabenstellung
Logo füge ich bei. Die Farben, das Design, die Schrift sollen dem Logo entsprechen (Grau, Violett-Pink Töne, moderne Schrift).

```html
<!DOCTYPE html>
<html lang="de">
<head>
<meta charset="utf-8">
<title>Über mich – Psychotherapeutische Praxis Andrea Hollmann</title>
<link href="https://fonts.googleapis.com/css2?family=Ubuntu:wght@300;400;500;700&display=swap" rel="stylesheet">
<style>
  :root {
    --violet: #7a5cb8;
    --pink: #c55aa3;
    --pink-soft: #d86fb2;
    --grey-text: #4a4a52;
    --grey-mid: #66666e;
    --page-bg: #f3f3f5;
    --card-bg: rgba(255,255,255,0.88);
    --footer-bg: #f1effa;
    --dot-blue: #4a7ee0;
    --dot-pink: #d45fa5;
  }
  * { box-sizing: border-box; margin: 0; padding: 0; }
  html, body { width: 1200px; height: 2274px; overflow: hidden; }
  body { position: relative; font-family: "Ubuntu", sans-serif; font-weight: 300; color: var(--grey-text); background: var(--page-bg); }

  .topbar { position: absolute; left: 0; top: 0; width: 1200px; height: 28px; background: linear-gradient(180deg, #7a5cb8, #a85fae); }
  .topbar__contact { position: absolute; top: 0; height: 28px; display: flex; align-items: center; gap: 6px; color: #fff; font-size: 8.5px; font-weight: 400; padding: 0 16px; border-left: 1px solid rgba(255,255,255,.25); }
  .topbar__phone { left: 541px; }
  .topbar__mail { left: 637px; border-right: 1px solid rgba(255,255,255,.25); }
  .topbar__menu { position: absolute; left: 968px; top: 10px; }

  .navrow { position: absolute; left: 0; top: 28px; width: 1200px; height: 41px; background: #fff; }
  .mainnav { position: absolute; left: 644px; top: 28px; height: 41px; display: flex; align-items: center; gap: 16px; font-size: 10.5px; font-weight: 400; color: var(--grey-mid); }
  .mainnav .is-active { color: var(--pink); }

  .brand { position: absolute; left: 219px; top: 0; width: 321px; height: 72px; background: #fff; box-shadow: 0 3px 10px rgba(0,0,0,.12); display: flex; align-items: center; padding-left: 24px; gap: 22px; color: var(--grey-text); font-weight: 400; }
  .brand__dot { width: 38px; height: 38px; border-radius: 50%; background: var(--violet); flex: none; }
  .brand__name { line-height: 1.25; }
  .brand__line1 { font-size: 13px; display: block; }
  .brand__line2 { font-size: 12px; display: block; letter-spacing: .3px; }
  .brand__line3 { font-size: 6.5px; display: block; letter-spacing: .5px; }

  .hero { position: absolute; left: 0; top: 69px; width: 1200px; height: 437px; overflow: hidden; }
  .hero__photo { position: absolute; inset: 0; background: linear-gradient(90deg, #a9a6a8 0%, #cdcbce 20%, #8a7d78 24%, #4a4444 38%, #d8d6da 56%, #e3e2e6 100%); }
  .hero__frame { position: absolute; left: 231px; top: 91px; width: 738px; height: 255px; border: 10px solid rgba(255,255,255,.75); }
  .hero__title { position: absolute; left: 594px; top: 186px; font-size: 54px; font-weight: 500; color: #fff; text-shadow: 0 2px 6px rgba(0,0,0,.35); }

  .career { position: absolute; left: 0; top: 506px; width: 1200px; height: 1166px; background: radial-gradient(ellipse at 55% 60%, #cfcdd2 0%, #e6e5e9 45%, #f4f4f6 80%); }
  .career__heading { position: absolute; left: 225px; top: 74px; display: flex; align-items: center; gap: 13px; font-size: 17.5px; color: var(--grey-text); }
  .career__heading::before { content: ""; width: 25px; height: 2px; background: var(--violet); }
  .timeline__line { position: absolute; left: 256px; top: 139px; width: 1.5px; height: 900px; background: var(--pink); }
  .timeline__item { position: absolute; left: 288px; width: 687px; height: 55px; background: var(--card-bg); box-shadow: 0 2px 6px rgba(0,0,0,.06); padding: 9px 10px; }
  .timeline__item::before { content: ""; position: absolute; left: -6px; top: 12px; width: 12px; height: 12px; background: var(--card-bg); transform: rotate(45deg); }
  .timeline__dot { position: absolute; left: -38px; top: 7px; width: 12px; height: 12px; border-radius: 50%; background: var(--dot-pink); border: 3px solid var(--dot-blue); }
  .timeline__year { font-size: 13px; font-weight: 400; color: var(--grey-text); display: block; margin-bottom: 6px; }
  .timeline__text { font-size: 9.5px; color: var(--grey-mid); }

  .contact { position: absolute; left: 0; top: 1672px; width: 1200px; height: 329px; background: linear-gradient(180deg, #dad9de, #e4e1e8 60%, #e7e1e8); text-align: center; }
  .contact__title { position: absolute; left: 0; width: 1200px; top: 66px; font-size: 24px; color: var(--grey-text); }
  .contact__rule { position: absolute; left: 585px; top: 98px; width: 30px; height: 2px; background: var(--violet); }
  .contact__text { position: absolute; left: 370px; width: 460px; top: 141px; font-size: 12.5px; line-height: 1.3; color: var(--grey-mid); }
  .contact__button { position: absolute; left: 516px; top: 219px; width: 168px; height: 30px; border-radius: 15px; background: var(--pink-soft); color: #fff; font-size: 9.5px; font-weight: 400; letter-spacing: .6px; display: flex; align-items: center; justify-content: center; gap: 8px; }

  .footer { position: absolute; left: 0; top: 2001px; width: 1200px; height: 202px; background: var(--footer-bg); }
  .footer__accent { position: absolute; left: 219px; top: 0; width: 500px; height: 3px; background: var(--pink); }
  .footer__brand { position: absolute; left: 243px; top: 37px; display: flex; align-items: center; gap: 14px; color: var(--grey-text); font-weight: 400; line-height: 1.25; }
  .footer__brand .brand__dot { width: 26px; height: 26px; }
  .footer__brand .l1 { font-size: 8.5px; display: block; }
  .footer__brand .l2 { font-size: 8px; display: block; }
  .footer__brand .l3 { font-size: 4.5px; display: block; }
  .footer__note { position: absolute; left: 243px; top: 126px; width: 450px; font-size: 8px; line-height: 1.7; color: var(--grey-mid); }
  .footer__note em { font-style: normal; color: var(--pink); }
  .footer__links { position: absolute; top: 39px; width: 106px; list-style: none; font-size: 8.2px; color: var(--grey-mid); }
  .footer__links li { padding: 3px 0 6px; border-bottom: 1px solid var(--pink-soft); line-height: 1.6; }
  .footer__links li:last-child { border-bottom: none; }
  .footer__links--main { left: 744px; }
  .footer__links--legal { left: 875px; }

  .bottombar { position: absolute; left: 0; top: 2203px; width: 1200px; height: 71px; background: linear-gradient(180deg, #7a5cb8, #c15fa8); }
  .bottombar__copy { position: absolute; left: 219px; top: 31px; font-size: 8px; font-weight: 500; color: #fff; }
  .bottombar__top { position: absolute; left: 953px; top: 22px; width: 28px; height: 28px; border: 1.5px solid #fff; display: flex; align-items: center; justify-content: center; }
</style>
</head>
<body>

<header>
  <div class="topbar">
    <div class="topbar__contact topbar__phone">
      <svg width="8" height="8" viewBox="0 0 24 24"><path fill="#fff" d="M6.6 10.8a15 15 0 0 0 6.6 6.6l2.2-2.2c.3-.3.7-.4 1-.2 1.1.4 2.3.6 3.6.6.6 0 1 .4 1 1V20c0 .6-.4 1-1 1A17 17 0 0 1 3 4c0-.6.4-1 1-1h3.5c.6 0 1 .4 1 1 0 1.3.2 2.5.6 3.6.1.3 0 .7-.2 1z"/></svg>
      0123 456 7890
    </div>
    <div class="topbar__contact topbar__mail">
      <svg width="9" height="7" viewBox="0 0 18 14"><rect x="1" y="1" width="16" height="12" fill="none" stroke="#fff" stroke-width="1.6"/><path d="M1 1l8 7 8-7" fill="none" stroke="#fff" stroke-width="1.6"/></svg>
      info@hollmann-therapie.de
    </div>
    <svg class="topbar__menu" width="12" height="9" viewBox="0 0 12 9"><rect width="12" height="1.5" fill="#fff"/><rect y="3.7" width="12" height="1.5" fill="#fff"/><rect y="7.4" width="12" height="1.5" fill="#fff"/></svg>
  </div>
  <div class="navrow"></div>
  <nav class="mainnav">
    <span>Startseite</span><span>Therapieangebot</span><span>Therapieverlauf</span><span class="is-active">Über mich</span><span>Kontakt</span>
  </nav>
  <div class="brand">
    <span class="brand__dot"></span>
    <span class="brand__name">
      <span class="brand__line1">Psychotherapeutische Praxis</span>
      <span class="brand__line2">DIPL.-PSYCH. ANDREA HOLLMANN</span>
      <span class="brand__line3">Psychologische Psychotherapeutin (VT)</span>
    </span>
  </div>
</header>

<section class="hero">
  <div class="hero__photo" role="img" aria-label="Porträtfoto der Therapeutin vor einem hellen, unscharfen Bürohintergrund"></div>
  <div class="hero__frame"></div>
  <h1 class="hero__title">Über mich</h1>
</section>

<section class="career" role="img" aria-label="Weich verschwommenes Foto als Hintergrund">
  <h2 class="career__heading">Ausbildung und beruflicher Werdegang:</h2>
  <div class="timeline__line"></div>

  <div class="timeline__item" style="top:126px"><span class="timeline__dot"></span><span class="timeline__year">Seit 2020</span><span class="timeline__text">Tätigkeit als Dozentin in der Weiterbildung von psychologischen Psychotherapeuten</span></div>
  <div class="timeline__item" style="top:190px"><span class="timeline__dot"></span><span class="timeline__year">Seit 2019</span><span class="timeline__text">Niedergelassen in eigener Praxis</span></div>
  <div class="timeline__item" style="top:255px"><span class="timeline__dot"></span><span class="timeline__year">2019</span><span class="timeline__text">Approbation zur Psychologischen Psychotherapeutin, Fachrichtung Verhaltenstherapie</span></div>
  <div class="timeline__item" style="top:319px"><span class="timeline__dot"></span><span class="timeline__year">2018 – 2019</span><span class="timeline__text">Praxisassistentin, Psychotherapeutische Praxis Taunusblick</span></div>
  <div class="timeline__item" style="top:384px"><span class="timeline__dot"></span><span class="timeline__year">2017 – 2018</span><span class="timeline__text">Stationspsychologin, Klinikum Rhein-Main, Station für Persönlichkeits- und Traumafolgestörungen</span></div>
  <div class="timeline__item" style="top:448px"><span class="timeline__dot"></span><span class="timeline__year">2015–2016</span><span class="timeline__text">Praktische Tätigkeit am Klinikum Rhein-Main, Klinik für Psychiatrie, Psychosomatik und Psychotherapie</span></div>
  <div class="timeline__item" style="top:513px"><span class="timeline__dot"></span><span class="timeline__year">2015–2019</span><span class="timeline__text">Weiterbildung zur Psychologischen Psychotherapeutin am Mainzer Institut für Verhaltenstherapie MIVT</span></div>
  <div class="timeline__item" style="top:577px"><span class="timeline__dot"></span><span class="timeline__year">2011 – 2017</span><span class="timeline__text">HR Business Partner, Nordavia Airlines AG, Frankfurt</span></div>
  <div class="timeline__item" style="top:641px"><span class="timeline__dot"></span><span class="timeline__year">2010</span><span class="timeline__text">Anerkennung Mag. Phil. und Diplom Arbeitspsychologie, Universität Donaustadt</span></div>
  <div class="timeline__item" style="top:706px"><span class="timeline__dot"></span><span class="timeline__year">2009</span><span class="timeline__text">Coaching Ausbildung, Akademie für Angewandte Psychologie, Berlin</span></div>
  <div class="timeline__item" style="top:770px"><span class="timeline__dot"></span><span class="timeline__year">1998 – 2010</span><span class="timeline__text">Coaching, Diagnostik, Training, Hollmann Consulting, Frankfurt und Wien</span></div>
  <div class="timeline__item" style="top:835px"><span class="timeline__dot"></span><span class="timeline__year">1995 – 1997</span><span class="timeline__text">Personalleiterin Germanic and Nordic Area, Velora Cosmetics</span></div>
  <div class="timeline__item" style="top:899px"><span class="timeline__dot"></span><span class="timeline__year">1991 – 1995</span><span class="timeline__text">Personalreferentin, Teamleiterin Lumière Beauté, Düsseldorf</span></div>
  <div class="timeline__item" style="top:963px"><span class="timeline__dot"></span><span class="timeline__year">1990</span><span class="timeline__text">Abschluss Diplom Psychologin</span></div>
  <div class="timeline__item" style="top:1028px"><span class="timeline__dot"></span><span class="timeline__year">1982 - 1990</span><span class="timeline__text">Studium der Psychologie an der Landesuniversität Lahntal</span></div>
</section>

<section class="contact" role="img" aria-label="Blasse Stadtansicht mit Hochhäusern als Hintergrund">
  <h2 class="contact__title">Kontakt</h2>
  <div class="contact__rule"></div>
  <p class="contact__text">Bei Fragen stehen wir Ihnen gerne zur Verfügung. Am besten erreichen Sie uns via E-Mail oder über das Kontaktformular.</p>
  <div class="contact__button">KONTAKT AUFNEHMEN
    <svg width="18" height="6" viewBox="0 0 18 6"><path d="M0 3h16M13 .5L16.5 3 13 5.5" fill="none" stroke="#fff" stroke-width="1"/></svg>
  </div>
</section>

<footer class="footer">
  <div class="footer__accent"></div>
  <div class="footer__brand">
    <span class="brand__dot"></span>
    <span>
      <span class="l1">Psychotherapeutische Praxis</span>
      <span class="l2">DIPL.-PSYCH. ANDREA HOLLMANN</span>
      <span class="l3">Psychologische Psychotherapeutin (VT)</span>
    </span>
  </div>
  <p class="footer__note">Sollten Sie mich nicht persönlich erreichen, hinterlassen Sie bitte eine Nachricht auf dem Anrufbeantworter oder senden Sie mir <em>eine e-mail</em></p>
  <ul class="footer__links footer__links--main">
    <li>Startseite</li><li>Therapieangebot</li><li>Therapieverlauf</li><li>Über mich</li><li>Kontakt</li>
  </ul>
  <ul class="footer__links footer__links--legal">
    <li>Impressum</li><li>Datenschutz</li><li>Cookie-Richtlinie</li><li>Datenschutzerklärung nach DSGVO</li>
  </ul>
</footer>

<div class="bottombar">
  <p class="bottombar__copy">© 2020 Psychotherapeutische Praxis - DIPL.-PSYCH. ANDREA HOLLMANN. Alle Rechte vorbehalten.</p>
  <div class="bottombar__top">
    <svg width="10" height="6" viewBox="0 0 10 6"><path d="M1 5l4-4 4 4" fill="none" stroke="#fff" stroke-width="1.5"/></svg>
  </div>
</div>

</body>
</html>
```